Grand Opening Banner needed for Marvelous Carpets and Home

My website is www.MarvelousCarpetsandHome.com (login with password 'plorka')

A full page banner 1000px X 500px with bright, lively colors and wording that shows an exciting GRAND OPENING celebration throughout the site. Banner needs to convey the following...

Grand Opening Sale
Runs through end of the month
Savings in every department
30 day Returns
Free Rug Pads with every rug
Free shipping.

Banner can be a simple background with graphics and text, or can be a room scene with rugs and furniture, or a grouping of rugs with text.

Some Ideas and Images can be taken from our vendor's websites, such as:

http://tbvendora.com/
http://dosmir.com/dosmir_2015/
http://www.pqmats.com/
http://zaverto.com/
http://shopbelwyn.com/

I also have quite a few room scene images available for use, if you desire.

Target Market(s)

Affluent women who care about stylish decor for their homes

Industry/Entity Type

Home And Garden

Requirements
Must have
• bold, vibrant appearance. Text that can be modified in Photoshop.
Nice to have
• HAND DRAWN, ARTIST STYLE ARTWORK IS GREATLY APPRECIATED.
• flat graphics and text with little to no 3 dimensional (shadow) effect. Font styles should be elegant/luxurious. An organic, scribbled, or painted style is nice in keeping with the handmade products that we sell.
• I am open to changing the color scheme of the website, to match your banner, so don't feel tied down to my existing colors.
Should not have
• nothing too modern or extreme in style.

```html
<!DOCTYPE html>
<html lang="en">
<head>
<meta charset="utf-8">
<title>Grand Opening Sale Banner</title>
<link rel="stylesheet" href="https://fonts.googleapis.com/css2?family=Marcellus&family=Cinzel:wght@500&display=swap">
<style>
  :root {
    --page: #ffffff;
    --rug-red: #9e1b1f;
    --rug-deep: #5e1014;
    --rug-cream: #e9dcc3;
    --rug-blue: #5f8bb3;
    --rug-orange: #d8553a;
    --title: #ffffff;
    --sale-red: rgba(200, 12, 22, 0.92);
    --sale-text: #f7e62a;
    --label-bg: rgba(255, 255, 255, 0.62);
    --label-text: #1b1413;
    --marker: #141010;
  }
  * { margin: 0; padding: 0; box-sizing: border-box; }
  html, body {
    width: 1198px; height: 1200px; overflow: hidden;
    background: var(--page);
  }
  .canvas { position: relative; width: 1198px; height: 1200px; background: var(--page); }
  .banner { position: absolute; left: 0; top: 0; width: 1198px; height: 604px; overflow: hidden; }
  .banner-photo {
    position: absolute; inset: 0;
    background:
      radial-gradient(ellipse 40% 45% at 22% 18%, var(--rug-orange) 0%, transparent 70%),
      radial-gradient(ellipse 35% 40% at 82% 72%, var(--rug-blue) 0%, transparent 70%),
      radial-gradient(ellipse 30% 35% at 40% 80%, var(--rug-cream) 0%, transparent 70%),
      radial-gradient(ellipse 45% 40% at 55% 30%, var(--rug-deep) 0%, transparent 75%),
      linear-gradient(135deg, var(--rug-red) 0%, var(--rug-deep) 45%, var(--rug-red) 100%);
  }
  .headline {
    position: absolute; left: 0; top: 240px; width: 1198px;
    text-align: center;
    font-family: "Marcellus", "Optima", serif;
    font-weight: 400;
    font-size: 100px; letter-spacing: 12px; line-height: 1;
    padding-left: 12px;
    color: var(--title);
    text-shadow: 3px 4px 6px rgba(0, 0, 0, 0.55);
  }
  .sale-badge {
    position: absolute; left: 937px; top: 43px; width: 230px; height: 230px;
    border-radius: 50%; background: var(--sale-red);
  }
  .sale-badge span {
    position: absolute; left: 0; top: 0; width: 100%; height: 100%;
    display: flex; align-items: center; justify-content: center;
    font-family: "Cinzel", "Times New Roman", serif; font-weight: 500;
    font-size: 70px; color: var(--sale-text);
    transform: rotate(-22deg);
  }
  .perks { list-style: none; }
  .perk {
    position: absolute; display: flex; align-items: center; height: 40px;
  }
  .perk-marker {
    width: 29px; height: 29px; margin-right: 22px; flex: none;
  }
  .perk-label {
    height: 40px; padding: 0 12px 0 14px;
    display: flex; align-items: center;
    background: var(--label-bg);
    font-family: "Marcellus", "Optima", sans-serif;
    font-size: 29px; letter-spacing: 0.6px; color: var(--label-text);
  }
</style>
</head>
<body>
<div class="canvas">
  <section class="banner">
    <div class="banner-photo" role="img" aria-label="Photograph of layered handwoven rugs in red, orange, cream and blue geometric patterns"></div>

    <div class="sale-badge"><span>SALE</span></div>

    <h1 class="headline">GRAND OPENING</h1>

    <ul class="perks">
      <li class="perk" style="left:165px; top:398px;">
        <svg class="perk-marker" viewBox="0 0 28 28"><rect width="28" height="28" fill="var(--marker)"/><rect x="9" y="9" width="10" height="10" fill="#fff" transform="rotate(45 14 14)"/></svg>
        <span class="perk-label">Runs through end of the month</span>
      </li>
      <li class="perk" style="left:165px; top:459px;">
        <svg class="perk-marker" viewBox="0 0 28 28"><rect width="28" height="28" fill="var(--marker)"/><rect x="9" y="9" width="10" height="10" fill="#fff" transform="rotate(45 14 14)"/></svg>
        <span class="perk-label">Free rug pads with every rug</span>
      </li>
      <li class="perk" style="left:165px; top:520px;">
        <svg class="perk-marker" viewBox="0 0 28 28"><rect width="28" height="28" fill="var(--marker)"/><rect x="9" y="9" width="10" height="10" fill="#fff" transform="rotate(45 14 14)"/></svg>
        <span class="perk-label">Savings in every department</span>
      </li>
      <li class="perk" style="left:762px; top:398px;">
        <svg class="perk-marker" viewBox="0 0 28 28"><rect width="28" height="28" fill="var(--marker)"/><rect x="9" y="9" width="10" height="10" fill="#fff" transform="rotate(45 14 14)"/></svg>
        <span class="perk-label">30 day returns</span>
      </li>
      <li class="perk" style="left:762px; top:459px;">
        <svg class="perk-marker" viewBox="0 0 28 28"><rect width="28" height="28" fill="var(--marker)"/><rect x="9" y="9" width="10" height="10" fill="#fff" transform="rotate(45 14 14)"/></svg>
        <span class="perk-label">Free shipping</span>
      </li>
    </ul>
  </section>
</div>
</body>
</html>
```